Flyer Design in Photoshop PSD format needed

Christmas Production Flyer - DL (Horizontal) 210 wide x 100 deep

Final file to have elements as layered .psd

We need a flyer design to promote our upcoming Christmas Production which will be based on a movie premier.

Target Market(s)

Young Families Young Adult

Industry/Entity Type

Movie

Requirements
Must have
• The design should look like a Movie poster or Movie Premier advertisement.
Movie Title: Lantern (Main line, focal point) of Tidings (Tag line, possibly italicised)
Dates: 16th and 18th of December
Time: 7pm
Tickets: Booking Online
Price: Free
Address: The Marlowe 412 Wattle St Newcastle
Presented by - Fellowship72

In the strip at the bottom
Parking available at Corvel and Rest Harbour
Starring: Baby Jesus, Mary, Joseph, Gabriel, Choir of Angels

(Colours - midnight style theme/night sky/stars - not heaps of colour - dramatic)
Nice to have
• Theme:
Like as on movie posters e.g. starring. Valmont Screen Gala premier glitz and glam. Monaco.
Star sitting above middle (left to right) shining down onto a manger
Black strip at the bottom like in a movie poster containing most of the info regarding the event.
Should not have
• Snow
Christmas Tree, bobbles and presents, tinsel not kitch

```html
<!DOCTYPE html>
<html lang="en">
<head>
<meta charset="utf-8">
<title>Lantern or Tidings – Christmas Production Flyer</title>
<link rel="stylesheet" href="https://fonts.googleapis.com/css2?family=Marcellus&family=Oswald:wght@300;400&family=Parisienne&display=swap">
<style>
  :root {
    --sky-deep: #05090b;
    --sky-mid: #14242a;
    --sky-haze: #4d6a72;
    --glow-core: #ffffff;
    --text-light: #ffffff;
    --text-soft: #e8eef0;
    --strip-bg: #070909;
    --strip-line: #8f9a9e;
    --cloth: #eeeae2;
    --straw: #b99a62;
    --wood: #5a4029;
    --wood-dark: #3a2818;
  }
  * { margin: 0; padding: 0; box-sizing: border-box; }
  html, body {
    width: 1200px;
    height: 572px;
    overflow: hidden;
    background: var(--sky-deep);
  }
  .flyer {
    position: relative;
    width: 1200px;
    height: 572px;
    overflow: hidden;
    color: var(--text-light);
  }
  .night-sky {
    position: absolute;
    inset: 0;
    background:
      radial-gradient(ellipse 260px 240px at 590px 400px, var(--glow-core) 0%, rgba(255,255,255,0.9) 30%, rgba(220,230,233,0.5) 60%, rgba(220,230,233,0) 100%),
      radial-gradient(ellipse 420px 380px at 590px 300px, rgba(150,176,184,0.7) 0%, rgba(77,106,114,0.45) 50%, rgba(20,36,42,0) 100%),
      radial-gradient(ellipse 900px 620px at 590px 300px, var(--sky-mid) 0%, var(--sky-deep) 100%);
  }
  .cast {
    position: absolute;
    top: 22px;
    left: 0;
    width: 1200px;
    height: 44px;
    list-style: none;
    font-family: "Oswald", sans-serif;
    font-weight: 400;
    font-size: 30px;
    letter-spacing: 0.5px;
    text-transform: uppercase;
  }
  .cast li {
    position: absolute;
    top: 0;
    transform: translateX(-50%);
    white-space: nowrap;
    line-height: 44px;
  }
  .cast-rule {
    position: absolute;
    top: 76px;
    left: 256px;
    width: 640px;
    height: 2px;
    background: linear-gradient(90deg, rgba(255,255,255,0) 0%, rgba(255,255,255,0.8) 15%, rgba(255,255,255,0.8) 85%, rgba(255,255,255,0) 100%);
  }
  .title {
    position: absolute;
    top: 80px;
    left: 0;
    width: 1200px;
    text-align: center;
    font-family: "Marcellus", serif;
    font-weight: 400;
    font-size: 118px;
    line-height: 1;
    letter-spacing: 4px;
    color: var(--text-light);
    text-shadow: 0 0 10px rgba(255,255,255,0.3);
  }
  .tagline {
    position: absolute;
    top: 206px;
    left: 0;
    width: 1200px;
    text-align: center;
    font-family: "Parisienne", cursive;
    font-size: 74px;
    line-height: 1.1;
    color: var(--text-light);
    text-shadow: 0 2px 5px rgba(0,0,0,0.3);
  }
  .manger {
    position: absolute;
    left: 436px;
    top: 324px;
    width: 300px;
    height: 214px;
    border-radius: 40% 40% 18% 18% / 30% 30% 12% 12%;
    background:
      radial-gradient(ellipse 120px 50px at 130px 40px, var(--cloth) 0%, rgba(238,234,226,0.6) 60%, rgba(238,234,226,0) 100%),
      linear-gradient(180deg, var(--straw) 0%, var(--wood) 45%, var(--wood-dark) 75%, rgba(58,40,24,0.15) 100%);
    opacity: 0.92;
  }
  .presenter {
    position: absolute;
    right: 72px;
    top: 486px;
    font-family: "Oswald", sans-serif;
    font-weight: 400;
    font-size: 22px;
    font-variant: small-caps;
    letter-spacing: 0.5px;
    color: var(--text-light);
    text-shadow: 0 1px 3px rgba(0,0,0,0.6);
  }
  .info-strip {
    position: absolute;
    left: 0;
    bottom: 0;
    width: 1200px;
    height: 44px;
    background: var(--strip-bg);
    border-top: 2px solid var(--strip-line);
    display: flex;
    justify-content: space-between;
    align-items: center;
    padding: 0 40px;
    list-style: none;
    font-family: "Oswald", sans-serif;
    font-weight: 300;
    font-size: 17px;
    font-variant: small-caps;
    letter-spacing: 0.2px;
    color: var(--text-soft);
    white-space: nowrap;
  }
</style>
</head>
<body>
  <main class="flyer">
    <div class="night-sky" role="img" aria-label="Dark starry night sky scattered with small white stars, with a bright white glow shining down on the centre"></div>

    <ul class="cast" aria-label="Starring">
      <li style="left:151px">Joseph</li>
      <li style="left:329px">Mary</li>
      <li style="left:553px">Baby Jesus</li>
      <li style="left:779px">Gabriel</li>
      <li style="left:1008px">Choir of Angels</li>
    </ul>
    <div class="cast-rule"></div>

    <h1 class="title">LANTERN</h1>
    <p class="tagline">or Tidings</p>

    <div class="manger" role="img" aria-label="Photo of a wooden manger on crossed legs, filled with straw and draped with a white cloth, lit from above"></div>

    <p class="presenter">Presented by - Fellowship72</p>

    <ul class="info-strip">
      <li>Dates: 16th and 18th of December</li>
      <li>Time: 7pm</li>
      <li>Tickets: Booking Online</li>
      <li>Price: Free</li>
      <li>Address: The Marlowe 412 Wattle St Newcastle</li>
      <li>Parking available at Corvel and Rest Harbour</li>
    </ul>
  </main>
</body>
</html>
```